BRIGHTHOLM ADVISORY powerpoint deck.

I REQUIRE A COMPANY POWERPOINT SLIDE DECK, WHICH MAY ALSO INCLUDE A NUMBER OF "MODELS". THIS MAY ALSO REQUIRE SOME FOLLOW UP WORK.

ATTACHED IS AN EXAMPLE SLIDE DECK FOR ONE OF MY CLIENTS. I would like to see a mock up of a few slides and then i can send a complete deck over.

Please note my website... www.brightholmadvisory.co.uk

I LOOK FORWARD TO SEEING YOUR DESIGN.

THANK YOU,

DAVID.

I work in the "learning and development"/ education/ leadership/ coaching industry

Leadership

Other font styles liked:
• century gothic

• ideally there would be some alignment to my website. www.brightholmadvisory.co.uk
• be fresh, clean, simple enough. look professional.
• how you present "models" i would come back for more work in the future if the work is good.
• too brash.

```html
<!DOCTYPE html>
<html lang="en">
<head>
<meta charset="utf-8">
<title>Brightholm Advisory – Slide Deck Overview</title>
<link href="https://fonts.googleapis.com/css2?family=Raleway:wght@300;400;600;700&display=swap" rel="stylesheet">
<style>
:root{
  --teal:#6bbdbb;
  --ink:#161616;
  --black:#000;
  --grey:#7d7d7d;
  --grey-soft:#9a9a9a;
  --muted:#b3b3b3;
  --line:#e2e2e2;
  --paper:#fff;
  --canvas:#ececec;
}
*{box-sizing:border-box;margin:0;padding:0}
html,body{width:1192px;height:1200px;overflow:hidden}
body{background:var(--canvas);font-family:"Raleway",sans-serif;color:var(--ink);position:relative}
.slide{position:absolute;width:478px;height:268px;background:var(--paper);overflow:hidden;transform:scale(.8164);transform-origin:0 0;box-shadow:0 1px 4px rgba(0,0,0,.18)}
.c1{left:3.3px}.c2{left:400px}.c3{left:796.8px}
.r1{top:13px}.r2{top:248.2px}.r3{top:483.3px}.r4{top:718.4px}.r5{top:953.6px}.r6{top:1188.7px}
.abs{position:absolute}
.title{position:absolute;left:20px;top:20px;font-size:22px;font-weight:400;letter-spacing:-.2px;color:var(--ink);line-height:1.1}
.title::after{content:"";display:block;width:42px;height:2px;background:var(--teal);margin-top:4px}
.brand{position:absolute;right:14px;top:26px;display:flex;align-items:center;gap:3px;font-size:5.6px;font-weight:700;letter-spacing:.4px;color:var(--ink)}
.brand i{width:9px;height:9px;border-radius:50%;background:var(--teal);display:block}
.brand.light{color:#fff;font-size:7px;top:40px;right:26px}
.foot{position:absolute;left:0;bottom:0;width:100%;height:14px;background:var(--black);color:#fff;font-size:4.6px;line-height:14px;padding-left:5px}
.foot .pg{position:absolute;right:16px;top:0;width:16px;height:14px;background:#2a2a2a;color:#aaa;text-align:center}
.foot .tl{position:absolute;right:0;top:0;width:16px;height:14px;background:var(--teal)}
.lorem{font-size:5.6px;line-height:1.4;color:var(--muted);font-weight:400}
.lorem p+p{margin-top:5px}
.h11{font-size:11px;font-weight:400;color:var(--ink);margin-bottom:6px}
.ic{width:20px;height:20px;border-radius:50%;background:var(--black);color:#fff;display:flex;align-items:center;justify-content:center;flex:none}
.ic.t{background:var(--teal)}
.ic svg{width:11px;height:11px}
.bl{position:absolute;display:flex;gap:7px;width:130px}
.bl b{display:block;font-size:8.5px;font-weight:400;color:var(--ink);margin-bottom:1px}
.bl.t b{color:var(--teal)}
.bl .lorem{font-size:5px}
.photo{position:absolute}
.divider-text{position:absolute;color:#fff;text-align:center}
.divider-text small{display:block;font-size:8px;font-weight:400}
.divider-text strong{display:block;font-size:21px;font-weight:300;line-height:1.15}
.divider-text span{display:block;font-size:10.5px;font-weight:300}
.col3{position:absolute;top:100px;width:88px;text-align:center}
.col3 .ring{width:24px;height:24px;border-radius:50%;border:1.5px solid #888;margin:0 auto 8px;display:flex;align-items:center;justify-content:center;color:#888}
.col3 .ring.t{border-color:var(--teal);color:var(--teal)}
.col3 .ring svg{width:12px;height:12px}
.col3 b{display:block;font-size:6.5px;font-weight:400;color:var(--ink);margin-bottom:2px}
.col3 b.t{color:var(--teal)}
.col3 .lorem{font-size:5px}
.vline{position:absolute;width:1px;background:var(--line)}
.col5{position:absolute;top:72px;width:70px;text-align:center}
.col5 .ic{width:19px;height:19px;margin:0 auto 3px}
.col5 b{display:block;font-size:6px;font-weight:400;color:var(--ink)}
.col5 b.t{color:var(--teal)}
.col5 .lorem{font-size:5px}
.plan{position:absolute;text-align:center}
.plan .head{color:#fff;display:flex;flex-direction:column;justify-content:center;align-items:center}
.plan .head strong{font-size:16px;font-weight:400;line-height:1}
.plan .head strong sup{font-size:9px;vertical-align:4px}
.plan .head small{font-size:4.5px}
.plan .body{background:#fff;font-size:5px;color:#555}
.plan .body div{border-bottom:1px solid #ececec;margin:0 10px;padding:5px 0}
.plan .body div:last-child{border:0}
.box4{position:absolute;top:101px;width:88px;height:117px;color:#fff;text-align:center;padding-top:22px}
.box4 .ring{width:22px;height:22px;border-radius:50%;border:1.5px solid #fff;margin:0 auto 16px;display:flex;align-items:center;justify-content:center}
.box4 .ring svg{width:11px;height:11px}
.box4 b{display:block;font-size:8px;font-weight:400;margin-bottom:4px}
.box4 p{font-size:5.8px;line-height:1.25;padding:0 14px}
.intro{position:absolute;text-align:center;font-size:5.8px;line-height:1.4;color:var(--muted)}
.ringcol{position:absolute;top:90px;width:80px;text-align:center}
.ringcol .big{width:58px;height:58px;border-radius:50%;border:5px solid var(--black);margin:0 auto 10px;display:flex;align-items:center;justify-content:center}
.ringcol .big svg{width:22px;height:22px}
.ringcol b{display:block;font-size:7px;font-weight:700;margin-bottom:4px}
.ringcol .lorem{font-size:5.4px}
.kp{position:absolute;top:114px;width:68px;height:68px;border-radius:50%;color:#fff;display:flex;flex-direction:column;align-items:center;justify-content:center;font-size:6px;line-height:1.1;text-align:center}
.kp svg{width:13px;height:13px;margin-bottom:3px}
.sv{position:absolute;left:0;top:0}
.label-box{position:absolute;left:30px;top:103px;width:107px;height:16px;background:var(--black);color:#fff;font-size:6px;line-height:16px;text-align:center;letter-spacing:.3px}
.legend{font-size:5px;fill:#444}
.cap{position:absolute;text-align:center;width:190px}
.cap b{display:block;font-size:7px;font-weight:400;color:var(--ink);margin-bottom:2px}
.cap .lorem{font-size:5.4px;color:#888}
</style>
</head>
<body>

<svg width="0" height="0" style="position:absolute" aria-hidden="true">
  <symbol id="i-bars" viewBox="0 0 16 16"><path fill="currentColor" d="M3 12h2V8H3zM7 12h2V5H7zM11 12h2V3h-2zM2 13h12v1H2z"/></symbol>
  <symbol id="i-crown" viewBox="0 0 16 16"><path fill="currentColor" d="M2 5l3 3 3-5 3 5 3-3-1 7H3zM3 13h10v1.4H3z"/></symbol>
  <symbol id="i-search" viewBox="0 0 16 16"><circle cx="6.5" cy="6.5" r="4" fill="none" stroke="currentColor" stroke-width="2"/><path d="M9.5 9.5l4 4" stroke="currentColor" stroke-width="2.2"/></symbol>
  <symbol id="i-pencil" viewBox="0 0 16 16"><path fill="currentColor" d="M3 13l1-3.2 7-7 2.2 2.2-7 7z"/></symbol>
  <symbol id="i-rocket" viewBox="0 0 16 16"><path fill="currentColor" d="M13 3c-3.5 0-6.5 2-7.8 6l1.8 1.8c4-1.3 6-4.3 6-7.8zM5 8.5l-2.5.8 2 2zM7.5 11l-.8 2.5 2-2zM3.5 11.5L2 14l2.5-1.5z"/></symbol>
  <symbol id="i-gear" viewBox="0 0 16 16"><circle cx="8" cy="8" r="2.6" fill="currentColor"/><circle cx="8" cy="8" r="5.2" fill="none" stroke="currentColor" stroke-width="2.4" stroke-dasharray="2 1.6"/></symbol>
  <symbol id="i-users" viewBox="0 0 16 16"><circle cx="5.2" cy="5.8" r="2" fill="currentColor"/><circle cx="10.8" cy="5.8" r="2" fill="currentColor"/><path fill="currentColor" d="M1.5 12c0-2 1.8-3.2 3.7-3.2S8.8 10 8.8 12zM7.2 12c0-2 1.8-3.2 3.6-3.2s3.7 1.2 3.7 3.2z"/></symbol>
  <symbol id="i-heart" viewBox="0 0 16 16"><path fill="currentColor" d="M8 13.5L2.8 8.3a2.8 2.8 0 014.4-3.5L8 5.6l.8-.8a2.8 2.8 0 014.4 3.5z"/></symbol>
  <symbol id="i-award" viewBox="0 0 16 16"><circle cx="8" cy="8" r="4" fill="currentColor"/><circle cx="8" cy="8" r="6.2" fill="none" stroke="currentColor" stroke-width="1.6" stroke-dasharray="1.5 1.2"/></symbol>
</svg>

<!-- Row 1 -->
<section class="slide c1 r1">
  <h2 class="title">Your Title</h2>
  <div class="brand"><i></i>BRIGHTHOLM ADVISORY</div>
  <div class="abs" style="left:19px;top:78px;width:124px">
    <h3 class="h11">Heading Goes Here</h3>
    <div class="lorem">
      <p>Lorem ipsum dolor sit amet, consectetur adipiscing elit, sed do eiusmod tempor incididunt ut labore et commodo consequat dolore magna aliqua.</p>
      <p>Duis aute irure dolor in reprehenderit in voluptate velit esse cillum dolore eu fugiat nulla pariatur.</p>
      <p>Ut enimad minim veniam, quis nostrud exercitation ullamco laboris nisi ut aliquip ex ea commodo consequat.</p>
    </div>
  </div>
  <div class="photo" role="img" aria-label="Photograph of glowing light bulbs on a dark grey background" style="left:153px;top:0;width:176px;height:254px;background:radial-gradient(circle at 35% 42%,#e9dfb8 0,#9c9683 16%,#5c5c58 40%,#363636 80%)"></div>
  <div class="bl" style="left:341px;top:76px"><span class="ic"><svg><use href="#i-search"/></svg></span><div><b>Your Text Here</b><div class="lorem">Lorem ipsum dolor sit amet, adipiscing elit, sed do eiusmod.</div></div></div>
  <div class="bl t" style="left:341px;top:116px"><span class="ic t"><svg><use href="#i-pencil"/></svg></span><div><b>Your Text Here</b><div class="lorem">Lorem ipsum dolor sit amet, adipiscing elit, sed do eiusmod.</div></div></div>
  <div class="bl" style="left:341px;top:155px"><span class="ic"><svg><use href="#i-rocket"/></svg></span><div><b>Your Text Here</b><div class="lorem">Lorem ipsum dolor sit amet, adipiscing elit, sed do eiusmod.</div></div></div>
  <div class="bl t" style="left:341px;top:194px"><span class="ic t"><svg><use href="#i-gear"/></svg></span><div><b>Your Text Here</b><div class="lorem">Lorem ipsum dolor sit amet, adipiscing elit, sed do eiusmod.</div></div></div>
  <footer class="foot">© 2017 BRIGHTHOLM ADVISORY All rights reserved<span class="pg">25</span><span class="tl"></span></footer>
</section>

<section class="slide c2 r1">
  <h2 class="title">Text &amp; Bullet Area</h2>
  <div class="brand"><i></i>BRIGHTHOLM ADVISORY</div>
  <div class="abs" style="left:23px;top:74px;width:124px">
    <h3 class="h11">Heading Goes Here</h3>
    <div class="lorem">
      <p>Lorem ipsum dolor sit amet, consectetur adipiscing elit, sed do eiusmod tempor incididunt ut labore et commodo consequat dolore magna aliqua.</p>
      <p>Duis aute irure dolor in reprehenderit in voluptate velit esse cillum dolore eu fugiat nulla pariatur.</p>
      <p>Ut enimad minim veniam, quis nostrud exercitation ullamco laboris nisi ut aliquip ex ea commodo consequat.</p>
    </div>
  </div>
  <div class="bl" style="left:176px;top:75px"><span class="ic"><svg><use href="#i-crown"/></svg></span><div><b>Your Text Here</b><div class="lorem">Lorem ipsum dolor sit amet, consectetur adipiscing elit, sed do eiusmod.</div></div></div>
  <div class="bl t" style="left:176px;top:114px"><span class="ic t"><svg><use href="#i-bars"/></svg></span><div><b>Your Text Here</b><div class="lorem">Lorem ipsum dolor sit amet, consectetur adipiscing elit, sed do eiusmod.</div></div></div>
  <div class="bl" style="left:176px;top:153px"><span class="ic"><svg><use href="#i-users"/></svg></span><div><b>Your Text Here</b><div class="lorem">Lorem ipsum dolor sit amet, consectetur adipiscing elit, sed do eiusmod.</div></div></div>
  <div class="bl t" style="left:176px;top:192px"><span class="ic t"><svg><use href="#i-award"/></svg></span><div><b>Your Text Here</b><div class="lorem">Lorem ipsum dolor sit amet, consectetur adipiscing elit, sed do eiusmod.</div></div></div>
  <div class="bl t" style="left:327px;top:75px"><span class="ic t"><svg><use href="#i-search"/></svg></span><div><b>Your Text Here</b><div class="lorem">Lorem ipsum dolor sit amet, consectetur adipiscing elit, sed do eiusmod.</div></div></div>
  <div class="bl" style="left:327px;top:114px"><span class="ic"><svg><use href="#i-pencil"/></svg></span><div><b>Your Text Here</b><div class="lorem">Lorem ipsum dolor sit amet, consectetur adipiscing elit, sed do eiusmod.</div></div></div>
  <div class="bl t" style="left:327px;top:153px"><span class="ic t"><svg><use href="#i-rocket"/></svg></span><div><b>Your Text Here</b><div class="lorem">Lorem ipsum dolor sit amet, consectetur adipiscing elit, sed do eiusmod.</div></div></div>
  <div class="bl" style="left:327px;top:192px"><span class="ic"><svg><use href="#i-gear"/></svg></span><div><b>Your Text Here</b><div class="lorem">Lorem ipsum dolor sit amet, consectetur adipiscing elit, sed do eiusmod.</div></div></div>
  <footer class="foot">© 2017 BRIGHTHOLM ADVISORY All rights reserved<span class="pg">26</span><span class="tl"></span></footer>
</section>

<section class="slide c3 r1">
  <div class="photo" role="img" aria-label="Dark photograph of hanging filament bulbs" style="inset:0;background:radial-gradient(circle at 70% 30%,#4a4a4a 0,#1f1f1f 40%,#0b0b0b 85%)"></div>
  <div class="brand light"><i></i>BRIGHTHOLM ADVISORY</div>
  <div class="divider-text" style="left:8px;top:136px;width:225px"><small>Divider Page</small><strong>Your Title Goes Here</strong><span>Your Subtitle Here</span></div>
</section>

<!-- Row 2 -->
<section class="slide c1 r2">
  <h2 class="title">Paragraph with Three Bullet</h2>
  <div class="brand"><i></i>BRIGHTHOLM ADVISORY</div>
  <p class="abs" style="left:22px;top:70px;width:400px;font-size:11px;line-height:1.3">This is place for your header text. Insert your text here, just replace this text with your own text</p>
  <div class="abs lorem" style="left:25px;top:122px;width:124px">
    <p>Lorem ipsum dolor sit amet, consectetur adipiscing elit, sed do eiusmod tempor incididunt ut labore et dolore magna aliqua. Ut enimad minim veniam, quis nostrud exercitation ullamco laboris nisi ut aliquip ex ea commodo consequat.</p>
    <p>Duis aute irure dolor in reprehenderit in voluptate velit esse cillum dolore eu fugiat nulla pariatur excepteur occaecat.</p>
  </div>
  <div class="vline" style="left:170px;top:108px;height:132px"></div>
  <div class="col3" style="left:182px"><div class="ring" style="border-color:#222;color:#222"><svg><use href="#i-bars"/></svg></div><b>Your Text Here</b><div class="lorem"><p>Lorem ipsum dolor sit amet, consectetur adipiscing elit, sed do eiusmod incididunt labore et aliqua.</p><p>Ut enimad minim veniam, quis nostrud exercitation ullamco laboris nisi ut commodo consequat.</p></div></div>
  <div class="col3 t" style="left:277px"><div class="ring t"><svg><use href="#i-crown"/></svg></div><b class="t">Your Text Here</b><div class="lorem"><p>Lorem ipsum dolor sit amet, consectetur adipiscing elit, sed do eiusmod incididunt labore et aliqua.</p><p>Ut enimad minim veniam, quis nostrud exercitation ullamco laboris nisi ut commodo consequat.</p></div></div>
  <div class="col3" style="left:373px"><div class="ring"><svg><use href="#i-rocket"/></svg></div><b>Your Text Here</b><div class="lorem"><p>Lorem ipsum dolor sit amet, consectetur adipiscing elit, sed do eiusmod incididunt labore et aliqua.</p><p>Ut enimad minim veniam, quis nostrud exercitation ullamco laboris nisi ut commodo consequat.</p></div></div>
  <footer class="foot">© 2017 BRIGHTHOLM ADVISORY All rights reserved<span class="pg">28</span><span class="tl"></span></footer>
</section>

<section class="slide c2 r2">
  <h2 class="title">Multiple Column Area</h2>
  <div class="brand"><i></i>BRIGHTHOLM ADVISORY</div>
  <div class="col5" style="left:26px"><div class="ic"><svg><use href="#i-gear"/></svg></div><b>Your Text Here</b><div class="lorem">Lorem ipsum consectetur adipiscing elit</div></div>
  <div class="col5" style="left:114px"><div class="ic t"><svg><use href="#i-rocket"/></svg></div><b class="t">Your Text Here</b><div class="lorem">Lorem ipsum consectetur adipiscing elit</div></div>
  <div class="col5" style="left:202px"><div class="ic" style="background:var(--grey)"><svg><use href="#i-search"/></svg></div><b>Your Text Here</b><div class="lorem">Lorem ipsum consectetur adipiscing elit</div></div>
  <div class="col5" style="left:291px"><div class="ic t"><svg><use href="#i-pencil"/></svg></div><b class="t">Your Text Here</b><div class="lorem">Lorem ipsum consectetur adipiscing elit</div></div>
  <div class="col5" style="left:378px"><div class="ic"><svg><use href="#i-bars"/></svg></div><b>Your Text Here</b><div class="lorem">Lorem ipsum consectetur adipiscing elit</div></div>
  <div class="abs" style="left:30px;top:124px;width:418px;height:1px;background:var(--line)"></div>
  <div class="abs" style="left:33px;top:160px;width:190px"><h3 class="h11" style="margin-bottom:2px">Heading Goes Here</h3><div class="lorem"><p>Lorem ipsum dolor sit amer, consectetur adipiscing elit, sed do eiusmod tempor incididunt ut labore et commodo consequat dolore magna aliqua.</p><p>Duis aute irure dolor in reprehenderit in voluptate velit esse cillum dolore eu fugiat nulla pariatur.</p></div></div>
  <div class="abs" style="left:258px;top:160px;width:190px"><h3 class="h11" style="margin-bottom:2px">Heading Goes Here</h3><div class="lorem"><p>Lorem ipsum dolor sit amer, consectetur adipiscing elit, sed do eiusmod tempor incididunt ut labore et commodo consequat dolore magna aliqua.</p><p>Duis aute irure dolor in reprehenderit in voluptate velit esse cillum dolore eu fugiat nulla pariatur.</p></div></div>
  <footer class="foot">© 2017 BRIGHTHOLM ADVISORY All rights reserved<span class="pg">29</span><span class="tl"></span></footer>
</section>

<section class="slide c3 r2">
  <h2 class="title" style="left:35px;top:23px">Monthly Subscription</h2>
  <div class="brand"><i></i>BRIGHTHOLM ADVISORY</div>
  <div class="abs" style="left:0;top:134px;width:478px;height:134px;background:var(--black)"></div>
  <div class="plan" style="left:70px;top:89px;width:95px">
    <div class="head" style="height:44px;background:var(--grey)"><strong><sup>$</sup>300</strong><small>per month</small></div>
    <div class="body" style="height:88px;padding-top:6px"><div>Single Edition</div><div>30gb Cloud Service</div><div>3 User</div><div>Free Update</div></div>
  </div>
  <div class="plan" style="left:178px;top:84px;width:122px">
    <div class="head" style="height:50px;background:var(--black)"><strong style="font-size:20px"><sup>$</sup>900</strong><small>per month</small></div>
    <div class="body" style="height:93px;padding-top:6px"><div>Business Edition</div><div>60gb Cloud Service</div><div>6 User</div><div>Free Update</div></div>
  </div>
  <div class="plan" style="left:312px;top:89px;width:96px">
    <div class="head" style="height:44px;background:var(--teal)"><strong><sup>$</sup>400</strong><small>per month</small></div>
    <div class="body" style="height:88px;padding-top:6px"><div>Single Edition</div><div>30gb Cloud Service</div><div>3 User</div><div>Free Update</div></div>
  </div>
</section>

<!-- Row 3 -->
<section class="slide c1 r3">
  <div class="photo" role="img" aria-label="Black and white photograph of a spiral staircase seen from above" style="inset:0;background:radial-gradient(circle at 50% 62%,#0c0c0c 0,#3a3a3a 18%,#6a6a6a 34%,#2c2c2c 55%,#5a5a5a 75%,#1a1a1a 100%)"></div>
  <div class="brand light"><i></i>BRIGHTHOLM ADVISORY</div>
  <div class="divider-text" style="left:8px;top:136px;width:225px"><small>Divider Page</small><strong>Your Title Goes Here</strong><span>Your Subtitle Here</span></div>
</section>

<section class="slide c2 r3">
  <h2 class="title" style="top:36px;line-height:.95">Video Title<br>Goes Here</h2>
  <div class="brand"><i></i>BRIGHTHOLM ADVISORY</div>
  <div class="abs lorem" style="left:21px;top:106px;width:114px">
    <p>Lorem ipsum dolor sit amer, consectetur adipiscing elit, sed do eiusmod tempor incididunt ut labore et commodo consequat dolore magna aliqua.</p>
    <p>Duis aute irure dolor in reprehenderit in voluptate velit esse cillum dolore eu fugiat nulla pariatur.</p>
    <p>Ut enimad minim veniam, quis nostrud exercitation ullamco laboris.</p>
  </div>
  <div class="photo" role="img" aria-label="Desktop monitor showing a video still of a business team" style="left:148px;top:42px;width:269px;height:194px;background:linear-gradient(180deg,#2b2b2b 0,#5d5550 40%,#b9b3ad 72%,#d9d9d9 74%,#e9e9e9 100%)"></div>
  <footer class="foot">© 2017 BRIGHTHOLM ADVISORY All rights reserved<span class="pg">32</span><span class="tl"></span></footer>
</section>

<section class="slide c3 r3">
  <h2 class="title">Four Column Area</h2>
  <div class="brand"><i></i>BRIGHTHOLM ADVISORY</div>
  <p class="intro" style="left:38px;top:73px;width:420px">Lorem ipsum dolor sit amet, consectetur adipiscing elit, sed do eiusmod tempor incididunt ut labore et dolore magna aliqua. Ut enimad minim veniam, quis nostrud exercitation ullamco laboris nisi ut aliquip ex ea commodo consequat.</p>
  <div class="box4" style="left:37px;background:var(--black)"><div class="ring"><svg><use href="#i-crown"/></svg></div><b>Your Text Here</b><p>Lorem Ipsum Dolor Sit Consectetur Adipiscing Elit</p></div>
  <div class="box4" style="left:142px;background:var(--teal)"><div class="ring"><svg><use href="#i-rocket"/></svg></div><b>Your Text Here</b><p>Lorem Ipsum Dolor Sit Consectetur Adipiscing Elit</p></div>
  <div class="box4" style="left:248px;background:var(--grey)"><div class="ring"><svg><use href="#i-award"/></svg></div><b>Your Text Here</b><p>Lorem Ipsum Dolor Sit Consectetur Adipiscing Elit</p></div>
  <div class="box4" style="left:353px;background:var(--black)"><div class="ring"><svg><use href="#i-bars"/></svg></div><b>Your Text Here</b><p>Lorem Ipsum Dolor Sit Consectetur Adipiscing Elit</p></div>
  <footer class="foot">© 2017 BRIGHTHOLM ADVISORY All rights reserved<span class="pg">33</span><span class="tl"></span></footer>
</section>

<!-- Row 4 -->
<section class="slide c1 r4">
  <h2 class="title">Four Column Area</h2>
  <div class="brand"><i></i>BRIGHTHOLM ADVISORY</div>
  <p class="intro" style="left:56px;top:60px;width:366px">Lorem ipsum dolor sit amet, consectetur adipiscing elit, sed do eiusmod tempor incididunt ut labore et dolore magna aliqua. Ut enimad minim veniam, quis nostrud exercitation ullamco laboris nisi ut aliquip ex ea commodo consequat.</p>
  <div class="ringcol" style="left:54px"><div class="big"><svg><use href="#i-bars"/></svg></div><b>COLUMN 1</b><div class="lorem">Lorem ipsum dolor sit amet, consectetur adipiscing elit, sed do eiusmod tempor incididunt ut labore et dolore magna aliqua.</div></div>
  <div class="ringcol" style="left:151px;color:var(--teal)"><div class="big" style="border-color:var(--teal)"><svg><use href="#i-crown"/></svg></div><b>COLUMN 2</b><div class="lorem">Lorem ipsum dolor sit amet, consectetur adipiscing elit, sed do eiusmod tempor incididunt ut labore et dolore magna aliqua.</div></div>
  <div class="ringcol" style="left:247px;color:var(--grey)"><div class="big" style="border-color:var(--grey)"><svg><use href="#i-rocket"/></svg></div><b>COLUMN 3</b><div class="lorem">Lorem ipsum dolor sit amet, consectetur adipiscing elit, sed do eiusmod tempor incididunt ut labore et dolore magna aliqua.</div></div>
  <div class="ringcol" style="left:344px"><div class="big"><svg><use href="#i-award"/></svg></div><b>COLUMN 4</b><div class="lorem">Lorem ipsum dolor sit amet, consectetur adipiscing elit, sed do eiusmod tempor incididunt ut labore et dolore magna aliqua.</div></div>
  <footer class="foot">© 2017 BRIGHTHOLM ADVISORY All rights reserved<span class="pg">34</span><span class="tl"></span></footer>
</section>

<section class="slide c2 r4">
  <h2 class="title">Key Points Area</h2>
  <div class="brand"><i></i>BRIGHTHOLM ADVISORY</div>
  <p class="intro" style="left:28px;top:80px;width:422px;text-align:left">Lorem ipsum dolor sit amet, consectetur adipiscing elit, sed do eiusmod tempor incididunt ut labore et dolore magna aliqua. Ut enimad minim veniam, quis nostrud exercitation ullamco laboris nisi ut aliquip ex ea commodo consequat.</p>
  <div class="kp" style="left:90px;background:var(--black);z-index:1"><svg><use href="#i-users"/></svg>Lorem<br>ipsum</div>
  <div class="kp" style="left:148px;background:var(--teal);z-index:2"><svg><use href="#i-pencil"/></svg>Lorem<br>ipsum</div>
  <div class="kp" style="left:206px;background:var(--grey);z-index:3"><svg><use href="#i-bars"/></svg>Lorem<br>ipsum</div>
  <div class="kp" style="left:263px;background:var(--teal);z-index:4"><svg><use href="#i-heart"/></svg>Lorem<br>ipsum</div>
  <div class="kp" style="left:320px;background:var(--black);z-index:5"><svg><use href="#i-crown"/></svg>Lorem<br>ipsum</div>
  <p class="intro" style="left:88px;top:197px;width:302px">Lorem ipsum dolor sit amet, consectetur adipiscing elit, sed do eiusmod tempor incididunt ut labore et dolore magna aliqua. Ut enimad minim veniam, quis nostrud exercitation ullamco laboris nisi ut aliquip ex ea commodo consequat.</p>
  <footer class="foot">© 2017 BRIGHTHOLM ADVISORY All rights reserved<span class="pg">35</span><span class="tl"></span></footer>
</section>

<section class="slide c3 r4">
  <h2 class="title">Workflow Area</h2>
  <div class="brand"><i></i>BRIGHTHOLM ADVISORY</div>
  <p class="intro" style="left:36px;top:72px;width:412px;text-align:left">Lorem ipsum dolor sit amet, consectetur adipiscing elit, sed do eiusmod tempor incididunt ut labore et dolore magna aliqua. Ut enimad minim veniam, quis nostrud exercitation ullamco laboris nisi ut aliquip ex ea commodo consequat.</p>
  <svg class="sv" width="478" height="268" viewBox="0 0 478 268" aria-hidden="true">
    <g fill="none" stroke-width="13">
      <path d="M40 150a39 39 0 0178 0" stroke="#000"/>
      <path d="M118 150a39 39 0 0078 0" stroke="#6bbdbb"/>
      <path d="M196 150a39 39 0 0178 0" stroke="#000"/>
      <path d="M274 150a39 39 0 0078 0" stroke="#6bbdbb"/>
      <path d="M352 150a39 39 0 0178 0" stroke="#000"/>
    </g>
    <g font-family="Raleway,sans-serif" font-size="5.5" text-anchor="middle">
      <circle cx="79" cy="149" r="7" fill="#000"/><text x="79" y="151" fill="#fff">1</text>
      <circle cx="157" cy="171" r="7" fill="#6bbdbb"/><text x="157" y="173" fill="#fff">2</text>
      <circle cx="235" cy="149" r="7" fill="#000"/><text x="235" y="151" fill="#fff">3</text>
      <circle cx="313" cy="171" r="7" fill="#6bbdbb"/><text x="313" y="173" fill="#fff">4</text>
      <circle cx="391" cy="149" r="7" fill="#000"/><text x="391" y="151" fill="#fff">5</text>
      <g font-size="7" font-weight="700">
        <text x="79" y="170" fill="#000">Data 1</text>
        <text x="157" y="115" fill="#6bbdbb">Data 2</text>
        <text x="235" y="170" fill="#000">Data 3</text>
        <text x="313" y="115" fill="#6bbdbb">Data 4</text>
        <text x="391" y="170" fill="#000">Data 5</text>
      </g>
      <g fill="#b3b3b3" font-size="4.8">
        <text x="79" y="178">Lorem ipsum dolor</text><text x="79" y="184">sit amet,</text><text x="79" y="190">consectetur</text><text x="79" y="196">adipiscing elit.</text>
        <text x="157" y="123">Lorem ipsum dolor</text><text x="157" y="129">sit amet,</text><text x="157" y="135">consectetur</text><text x="157" y="141">adipiscing elit.</text>
        <text x="235" y="178">Lorem ipsum dolor</text><text x="235" y="184">sit amet,</text><text x="235" y="190">consectetur</text><text x="235" y="196">adipiscing elit.</text>
        <text x="313" y="123">Lorem ipsum dolor</text><text x="313" y="129">sit amet,</text><text x="313" y="135">consectetur</text><text x="313" y="141">adipiscing elit.</text>
        <text x="391" y="178">Lorem ipsum dolor</text><text x="391" y="184">sit amet,</text><text x="391" y="190">consectetur</text><text x="391" y="196">adipiscing elit.</text>
      </g>
    </g>
  </svg>
  <footer class="foot">© 2017 BRIGHTHOLM ADVISORY All rights reserved<span class="pg">36</span><span class="tl"></span></footer>
</section>

<!-- Row 5 -->
<section class="slide c1 r5">
  <h2 class="title">Timeline</h2>
  <div class="brand"><i></i>BRIGHTHOLM ADVISORY</div>
  <svg class="sv" width="478" height="268" viewBox="0 0 478 268" aria-hidden="true">
    <line x1="64" y1="127" x2="412" y2="127" stroke="#cfcfcf" stroke-width="1"/>
    <g stroke="#cfcfcf" stroke-width="1">
      <line x1="123" y1="100" x2="123" y2="127"/><line x1="237" y1="100" x2="237" y2="127"/><line x1="351" y1="100" x2="351" y2="127"/>
      <line x1="180" y1="127" x2="180" y2="143"/><line x1="294" y1="127" x2="294" y2="143"/>
    </g>
    <g font-family="Raleway,sans-serif" text-anchor="middle" fill="#fff">
      <circle cx="64" cy="122" r="25" fill="#000"/><text x="64" y="124" font-size="10">2010</text><text x="64" y="130" font-size="3.6">Your Text</text><text x="64" y="134" font-size="3.6">Goes Here</text>
      <circle cx="123" cy="78" r="25" fill="#6bbdbb"/><text x="123" y="80" font-size="10">2011</text><text x="123" y="86" font-size="3.6">Your Text</text><text x="123" y="90" font-size="3.6">Goes Here</text>
      <circle cx="180" cy="168" r="25" fill="#7d7d7d"/><text x="180" y="170" font-size="10">2012</text><text x="180" y="176" font-size="3.6">Your Text</text><text x="180" y="180" font-size="3.6">Goes Here</text>
      <circle cx="237" cy="78" r="25" fill="#000"/><text x="237" y="80" font-size="10">2013</text><text x="237" y="86" font-size="3.6">Your Text</text><text x="237" y="90" font-size="3.6">Goes Here</text>
      <circle cx="294" cy="168" r="25" fill="#7d7d7d"/><text x="294" y="170" font-size="10">2014</text><text x="294" y="176" font-size="3.6">Your Text</text><text x="294" y="180" font-size="3.6">Goes Here</text>
      <circle cx="351" cy="78" r="25" fill="#6bbdbb"/><text x="351" y="80" font-size="10">2015</text><text x="351" y="86" font-size="3.6">Your Text</text><text x="351" y="90" font-size="3.6">Goes Here</text>
      <circle cx="408" cy="122" r="25" fill="#000"/><text x="408" y="124" font-size="10">2016</text><text x="408" y="130" font-size="3.6">Your Text</text><text x="408" y="134" font-size="3.6">Goes Here</text>
    </g>
    <path d="M418 148c4 8 2 14-6 18" fill="none" stroke="#000" stroke-width=".8"/>
  </svg>
  <div class="abs" style="left:20px;top:211px;width:210px"><b style="display:block;font-size:8.5px;font-weight:400">Your Text Goes Here</b><div class="lorem" style="font-size:5px">Lorem ipsum dolor sit amet, consectetur adipiscing elit, sed do eiusmod tempor incididunt ut labore et dolore magna aliqua.</div></div>
  <div class="abs" style="left:330px;top:169px;width:100px;text-align:right"><b style="display:block;font-size:8.5px;font-weight:400">Your Text Goes Here</b><div class="lorem" style="font-size:5px">Lorem ipsum dolor sit amet, consectetur adipiscing elit, sed do eiusmod tempor incididunt ut labore et dolore magna aliqua.</div></div>
  <footer class="foot">© 2017 BRIGHTHOLM ADVISORY All rights reserved<span class="pg">37</span><span class="tl"></span></footer>
</section>

<section class="slide c2 r5">
  <h2 class="title">This Is Line Chart Slide</h2>
  <div class="brand"><i></i>BRIGHTHOLM ADVISORY</div>
  <div class="label-box">CREATIVE TEXT HERE</div>
  <div class="abs lorem" style="left:36px;top:140px;width:116px;font-size:6px"><span style="color:#555">Lorem Ipsum dolor</span> sit amer, consectetur adipiscing elit, sed do eiusmod tempor incididunt ut labore et commodo consequat dolore magna aliqua.</div>
  <svg class="sv" width="478" height="268" viewBox="0 0 478 268" aria-hidden="true">
    <g font-family="Raleway,sans-serif" font-size="4.4" fill="#777" text-anchor="end">
      <text x="200" y="69">5</text><text x="200" y="84">4.5</text><text x="200" y="98">4</text><text x="200" y="113">3.5</text><text x="200" y="128">3</text><text x="200" y="142">2.5</text><text x="200" y="157">2</text><text x="200" y="172">1.5</text><text x="200" y="186">1</text><text x="200" y="201">0.5</text><text x="200" y="216">0</text>
    </g>
    <line x1="206" y1="214" x2="452" y2="214" stroke="#ccc" stroke-width=".8"/>
    <g font-family="Raleway,sans-serif" font-size="4.4" fill="#777" text-anchor="middle">
      <text x="237" y="224">Category 1</text><text x="299" y="224">Category 2</text><text x="361" y="224">Category 3</text><text x="422" y="224">Category 4</text>
    </g>
    <polyline points="237,86 299,141 361,112 422,81" fill="none" stroke="#161616" stroke-width="2"/>
    <polyline points="237,156 299,85 361,158 422,132" fill="none" stroke="#6bbdbb" stroke-width="2"/>
    <g fill="#161616"><circle cx="299" cy="141" r="2.2"/><circle cx="361" cy="112" r="2.2"/><circle cx="422" cy="81" r="2.2"/></g>
    <circle cx="299" cy="85" r="2.2" fill="#6bbdbb"/>
  </svg>
  <footer class="foot">© 2017 BRIGHTHOLM ADVISORY All rights reserved<span class="pg">38</span><span class="tl"></span></footer>
</section>

<section class="slide c3 r5">
  <h2 class="title">Market Performance</h2>
  <div class="brand"><i></i>BRIGHTHOLM ADVISORY</div>
  <svg class="sv" width="478" height="268" viewBox="0 0 478 268" aria-hidden="true">
    <defs>
      <g id="bar-chart">
        <g class="legend" font-family="Raleway,sans-serif">
          <rect x="84" y="55" width="3" height="3" fill="#000"/><text x="89" y="58">Profit</text>
          <rect x="107" y="55" width="3" height="3" fill="#6bbdbb"/><text x="112" y="58">Cost</text>
          <rect x="127" y="55" width="3" height="3" fill="#888"/><text x="132" y="58">Sales</text>
        </g>
        <path d="M28 170h180l8-6H36z" fill="#f0f0f0"/>
        <g>
          <rect x="38" y="105" width="8" height="65" fill="#000"/><rect x="46" y="110" width="8" height="60" fill="#6bbdbb"/><rect x="54" y="127" width="8" height="43" fill="#888"/>
          <rect x="82" y="122" width="8" height="48" fill="#000"/><rect x="90" y="130" width="8" height="40" fill="#6bbdbb"/><rect x="98" y="135" width="8" height="35" fill="#888"/>
          <rect x="126" y="100" width="8" height="70" fill="#000"/><rect x="134" y="112" width="8" height="58" fill="#6bbdbb"/><rect x="142" y="90" width="8" height="80" fill="#888"/>
          <rect x="170" y="72" width="8" height="98" fill="#000"/><rect x="178" y="112" width="8" height="58" fill="#6bbdbb"/><rect x="186" y="92" width="8" height="78" fill="#888"/>
        </g>
        <g fill="#000" opacity=".25">
          <path d="M62 127l3-2v45h-3zM106 135l3-2v37h-3zM150 90l3-2v82h-3zM194 92l3-2v80h-3z"/>
        </g>
        <g font-family="Raleway,sans-serif" font-size="5" fill="#444" text-anchor="middle">
          <text x="50" y="181">2011</text><text x="94" y="181">2012</text><text x="138" y="181">2013</text><text x="182" y="181">2014</text>
        </g>
      </g>
    </defs>
    <use href="#bar-chart"/>
    <use href="#bar-chart" x="234"/>
  </svg>
  <div class="cap" style="left:25px;top:192px"><b>Income</b><div class="lorem">Nullam eu tempor purus. Nunc a leo magna, sit amet consequat risus. Etiam faucibus tortor a ipsum vehicula sed hendrerit eros suscipit. Mauris quam dolor, cursus at porta et, luctus eget purus.</div></div>
  <div class="cap" style="left:259px;top:192px"><b>Cost Efficiency</b><div class="lorem">Nullam eu tempor purus. Nunc a leo magna, sit amet consequat risus. Etiam faucibus tortor a ipsum vehicula sed hendrerit eros suscipit. Mauris quam dolor, cursus at porta et, luctus eget purus.</div></div>
  <footer class="foot">© 2017 BRIGHTHOLM ADVISORY All rights reserved<span class="pg">39</span><span class="tl"></span></footer>
</section>

<!-- Row 6 (continues below the canvas edge) -->
<section class="slide c1 r6"><div class="brand" style="top:4px"><i></i>BRIGHTHOLM ADVISORY</div></section>
<section class="slide c2 r6"><div class="brand" style="top:4px"><i></i>BRIGHTHOLM ADVISORY</div></section>
<section class="slide c3 r6"><div class="brand" style="top:4px"><i></i>BRIGHTHOLM ADVISORY</div></section>

</body>
</html>
```